Upmarket Bathroom and Kitchen ware supplier needs a classy business card design

We are a company based in Fiji, we sell plumbing ware (Kitchen and bathroom taps, Basins,showers, toilets etc) through up market show rooms to individuals and directly through Architects and designers of resorts and holiday houses for new builds and renovations. we are wanting to upgrade our over all look and brand. we are starting with a new logo but will be rebranding the whole business. This project is for a business card design for my management and tales team I would like it to be dark, classy and interesting

Target Market(s)

Resort directors and Management, High end holiday home owners

Contact Information for Business Card

Gavin Threlkeld
Director
+64219473518

Colors

Designer to choose colors to be used in the design.

Requirements
Must have
• Must have an upmarket appearance I like darker charcoal shades but will be guided by the designers
• Please any catch phrases like "Crafting remarkable living rooms" this belongs tpo one of our suppliers so can not be used.
Nice to have
• Double sided, so front dedicated to logo provided and back info about the business and the person.

```html
<!DOCTYPE html>
<html lang="en">
<head>
<meta charset="utf-8">
<title>Solace Interiors – Business Card</title>
<link href="https://fonts.googleapis.com/css2?family=Open+Sans:wght@400;700&family=Montserrat:wght@300&display=swap" rel="stylesheet">
<style>
  :root {
    --page: #2a2c30;
    --card-black: #070707;
    --card-charcoal: #1b1b1c;
    --pattern-deep: #0c0c0d;
    --pattern-soft: #161617;
    --white: #ffffff;
    --silver: #c9c9c9;
  }
  * { margin: 0; padding: 0; box-sizing: border-box; }
  html, body { width: 1200px; height: 900px; overflow: hidden; }
  body {
    background: var(--page);
    display: flex;
    flex-direction: column;
    align-items: center;
    justify-content: center;
    gap: 48px;
    font-family: "Open Sans", sans-serif;
  }
  .card {
    position: relative;
    width: 640px;
    height: 366px;
    border-radius: 4px;
    overflow: hidden;
    background: var(--card-black);
    box-shadow: 0 14px 30px rgba(0,0,0,.45);
  }
  .card-art { position: absolute; inset: 0; width: 100%; height: 100%; }

  /* Logo side */
  .brand-pattern {
    position: absolute; inset: 0;
    background: linear-gradient(135deg, var(--pattern-soft), var(--pattern-deep) 70%);
  }
  .brand-lockup {
    position: absolute; inset: 0;
    display: flex; align-items: center; justify-content: center; gap: 12px;
  }
  .brand-dot {
    width: 10px; height: 10px; border-radius: 50%;
    background: var(--silver);
  }
  .brand-name {
    font-family: "Montserrat", sans-serif;
    font-weight: 300;
    font-size: 24px;
    letter-spacing: 7px;
    color: var(--silver);
  }

  /* Info side */
  .info-brand {
    position: absolute; left: 40px; top: 52px;
    display: flex; align-items: center; gap: 10px;
  }
  .info-brand .brand-name { font-size: 22px; letter-spacing: 6px; }
  .contact {
    position: absolute; right: 34px; bottom: 34px;
    text-align: right; color: var(--white);
  }
  .contact-name { font-weight: 700; font-size: 25px; letter-spacing: .5px; line-height: 1.1; }
  .contact-role { font-size: 17px; margin-bottom: 10px; }
  .contact-line {
    display: flex; align-items: center; justify-content: flex-end; gap: 10px;
    font-size: 17px; line-height: 1.5;
  }
  .contact-line b { font-weight: 700; }
  .contact-icon { width: 16px; height: 16px; flex: none; }
</style>
</head>
<body>

  <section class="card card-front">
    <div class="brand-pattern" role="img" aria-label="Faint repeating brand monogram pattern"></div>
    <div class="brand-lockup">
      <span class="brand-dot"></span>
      <span class="brand-name">SOLACE INTERIORS</span>
    </div>
  </section>

  <section class="card card-back">
    <svg class="card-art" viewBox="0 0 640 366" aria-hidden="true">
      <rect width="640" height="366" fill="var(--card-black)"/>
      <path d="M0,212 C190,204 370,150 640,44 L640,366 L0,366 Z" fill="var(--card-charcoal)"/>
      <path d="M0,182 C190,178 380,118 640,10 L640,44 C370,150 190,204 0,212 Z" fill="var(--white)"/>
      <path d="M0,192 C170,186 330,150 520,80 C360,160 180,198 0,202 Z" fill="var(--card-black)"/>
      <path d="M0,160 C150,162 300,130 470,70 C310,140 150,170 0,168 Z" fill="var(--white)"/>
    </svg>

    <div class="info-brand">
      <span class="brand-dot"></span>
      <span class="brand-name">SOLACE INTERIORS</span>
    </div>

    <div class="contact">
      <div class="contact-name">GAVIN THRELKELD</div>
      <div class="contact-role">Director</div>
      <div class="contact-line">+642 1947 3518
        <svg class="contact-icon" viewBox="0 0 16 16"><path d="M3.5 1.5l2.5 3-1.5 1.5c.8 2 2.5 3.7 4.5 4.5l1.5-1.5 3 2.5-1.5 2.5C7 13.5 2.5 9 1 3z" fill="var(--white)"/></svg>
      </div>
      <div class="contact-line">info@solaceinteriors.com
        <svg class="contact-icon" viewBox="0 0 16 16"><rect x="1" y="3" width="14" height="10" fill="var(--white)"/><path d="M1 3l7 6 7-6" fill="none" stroke="var(--card-charcoal)" stroke-width="1.3"/></svg>
      </div>
      <div class="contact-line"><span>www.<b>solaceinteriors</b>.com</span>
        <svg class="contact-icon" viewBox="0 0 16 16"><circle cx="8" cy="8" r="7" fill="var(--white)"/><g fill="none" stroke="var(--card-charcoal)" stroke-width="1"><ellipse cx="8" cy="8" rx="3" ry="7"/><path d="M1 8h14M2.5 4.5h11M2.5 11.5h11"/></g></svg>
      </div>
    </div>
  </section>

</body>
</html>
```